Moving Company Website

We need a webdesign for an established moving company in the Bay Area. We have chosen a wordpress template (see attached) and would like to revamp the design to give it a touch and feel of a leading moving company.
The design should be inspired by the following companies:
http://www.brightvanline.com/
http://www.kpcarriers.com/
Updates

The design should be based on the following WordPress template:

http://www.layoutforge.com/demo/35782.html

And based on the image I have attached.

We will get the template PSD after we will choose a designer.

Thanks
Marcus 

Industry/Entity Type

Moving Company

Requirements
Must have
• Request a quote form must be implemented in all pages
inner pages with destinations

```html
<!DOCTYPE html>
<html lang="en">
<head>
<meta charset="utf-8">
<title>Harborline Movers — Home</title>
<link rel="stylesheet" href="https://fonts.googleapis.com/css2?family=Roboto+Condensed:wght@300;400;700&family=Arimo:wght@400&display=swap">
<style>
  :root {
    --ink: #222222;
    --text: #3a3a3a;
    --nav: #444444;
    --page: #ffffff;
    --band: #f1f1f1;
    --rule: #c9c9c9;
    --panel: #93b2ba;
    --field: #ffffff;
    --field-text: #6b6b6b;
    --submit-text: #4f9a2f;
    --icon: #c4c4c4;
    --icon-dark: #9a9a9a;
    --footer-top: #e2e2e2;
    --footer-bottom: #f4f4f4;
  }
  * { box-sizing: border-box; margin: 0; padding: 0; }
  html, body { width: 851px; height: 1200px; overflow: hidden; background: var(--page); }
  body { position: relative; font-family: "Arimo", Arial, sans-serif; color: var(--text); }

  .brand { position: absolute; left: 58px; top: 40px; font-family: "Roboto Condensed", sans-serif; font-weight: 700; font-size: 22px; line-height: 24px; color: var(--ink); text-transform: uppercase; letter-spacing: 0.5px; }

  .social { position: absolute; left: 609px; top: 26px; display: flex; align-items: center; gap: 9px; }
  .social-label { font-family: "Roboto Condensed", sans-serif; font-size: 14px; color: var(--ink); text-transform: uppercase; margin-right: 2px; }
  .social-dot { width: 25px; height: 25px; border-radius: 50%; background: var(--icon); }

  .main-nav { position: absolute; right: 32px; top: 73px; display: flex; gap: 18px; font-family: "Roboto Condensed", sans-serif; font-weight: 300; font-size: 14.5px; text-transform: uppercase; color: var(--nav); }
  .main-nav a { color: inherit; text-decoration: none; }
  .main-nav .current { color: var(--ink); font-weight: 400; text-decoration: underline; text-underline-offset: 3px; }

  .hero { position: absolute; left: 33px; top: 112px; width: 585px; height: 342px; background: linear-gradient(100deg, #e8dcc4 0%, #7a8a92 28%, #506069 55%, #9aa9b2 80%, #c9d2d6 100%); overflow: hidden; }
  .hero-caption { position: absolute; left: 0; bottom: 0; width: 100%; height: 46px; background: rgba(40,45,50,0.35); color: #fff; font-family: "Arimo", Arial, sans-serif; font-size: 23px; line-height: 46px; padding-left: 17px; }

  .estimate { position: absolute; left: 634px; top: 112px; width: 182px; height: 342px; background: var(--panel); padding: 18px 0 0 21px; }
  .estimate h2 { font-family: "Roboto Condensed", sans-serif; font-weight: 700; font-size: 18px; color: #fff; text-transform: uppercase; margin: 0 0 15px -6px; }
  .estimate .field { width: 141px; height: 25px; background: var(--field); border: 1px solid #d8d8d8; font-size: 12px; color: var(--field-text); line-height: 23px; padding-left: 8px; margin-bottom: 12.5px; position: relative; }
  .estimate .select-arrow { position: absolute; right: 0; top: 0; width: 24px; height: 23px; border-left: 1px solid #ccc; background: #efefef; }
  .estimate .submit { width: 141px; height: 24px; margin-top: 16px; border-radius: 4px; background: linear-gradient(#ffffff, #e7e7e7); border: 1px solid #bdbdbd; text-align: center; font-family: "Roboto Condensed", sans-serif; font-weight: 700; font-size: 12px; line-height: 22px; color: var(--submit-text); text-transform: uppercase; }

  .feature { position: absolute; top: 478px; width: 184px; }
  .feature h3 { font-family: "Roboto Condensed", sans-serif; font-weight: 700; font-size: 24px; letter-spacing: 1px; color: var(--ink); text-transform: uppercase; height: 46px; }
  .feature .photo { width: 184px; height: 134px; position: relative; }
  .feature p { margin-top: 31px; font-size: 11.5px; line-height: 16px; color: var(--text); height: 118px; }
  .more { display: flex; align-items: center; gap: 14px; font-family: "Roboto Condensed", sans-serif; font-size: 14px; color: var(--ink); }
  .more svg { display: block; }

  .about { position: absolute; left: 0; top: 855px; width: 851px; height: 288px; background: var(--band); border-top: 1px solid var(--rule); }
  .about-col { position: absolute; top: 30px; width: 382px; }
  .about-col h2 { font-family: "Roboto Condensed", sans-serif; font-weight: 700; font-size: 38px; color: var(--ink); text-transform: uppercase; line-height: 44px; margin-bottom: 16px; letter-spacing: -0.3px; }
  .about-col p { font-size: 13px; line-height: 20.5px; color: var(--text); }

  .site-footer { position: absolute; left: 0; top: 1143px; width: 851px; height: 57px; background: linear-gradient(var(--footer-top), var(--footer-bottom)); }
  .footer-brand { position: absolute; left: 40px; top: 20px; font-family: "Roboto Condensed", sans-serif; font-weight: 700; font-size: 13px; color: var(--ink); text-transform: uppercase; }
  .copyright { position: absolute; left: 150px; top: 22px; font-size: 10px; color: var(--text); }
  .footer-nav { top: 24px; right: 37px; font-size: 14px; gap: 16px; }
</style>
</head>
<body>

<header>
  <div class="brand">Harborline<br>Movers</div>
  <div class="social">
    <span class="social-label">Socialize with us:</span>
    <span class="social-dot"></span><span class="social-dot"></span><span class="social-dot"></span>
  </div>
  <nav class="main-nav">
    <a class="current" href="#">Home</a><a href="#">About us</a><a href="#">Services</a><a href="#">Products</a><a href="#">Partners</a><a href="#">News</a><a href="#">Contacts</a>
  </nav>
</header>

<section class="hero" role="img" aria-label="Truck speeding along a highway under a dramatic sky">
  <div class="hero-caption">Lorem ipsum dolor sit amet, consectetur adipiscing elit.</div>
</section>

<aside class="estimate">
  <h2>Request an estimate</h2>
  <div class="field">First name</div>
  <div class="field">Last name</div>
  <div class="field">Phone number</div>
  <div class="field">Email</div>
  <div class="field">Select Service
    <span class="select-arrow"><svg width="24" height="23" viewBox="0 0 24 23"><path d="M7 9h10l-5 6z" fill="#333"/></svg></span>
  </div>
  <div class="submit">Submit</div>
</aside>

<section class="feature" style="left:33px">
  <h3>Moving</h3>
  <div class="photo" role="img" aria-label="Moving truck on an open road" style="background:linear-gradient(#cdd6db,#9aa6ad 60%,#5d6468)"></div>
  <p>Lorem ipsum dolor sit amet, consectetur adipiscing elit. Donec tempor elementum orci semper convallis. Vestibulum molestie cursus eros, sit amet vulputate nisl congue non.</p>
  <div class="more">more info <svg width="17" height="17" viewBox="0 0 17 17"><circle cx="8.5" cy="8.5" r="8.5" fill="var(--icon)"/><path d="M7 5l4 3.5-4 3.5z" fill="#fff"/></svg></div>
</section>

<section class="feature" style="left:233px">
  <h3>Storage</h3>
  <div class="photo" role="img" aria-label="Warehouse shelving with a forklift" style="background:linear-gradient(135deg,#c9b79a,#8e7a60 55%,#b35a3a)"></div>
  <p>Donec dui dolor, ultrices a tincidunt in, fermentum id ante. Suspendisse nibh velit, congue quis accumsan et, interdum sed nisi. Lorem ipsum dolor sit amet, consectetur adipiscing elit.</p>
  <div class="more">more info <svg width="17" height="17" viewBox="0 0 17 17"><circle cx="8.5" cy="8.5" r="8.5" fill="var(--icon)"/><path d="M7 5l4 3.5-4 3.5z" fill="#fff"/></svg></div>
</section>

<section class="feature" style="left:433px">
  <h3>Services</h3>
  <div class="photo" role="img" aria-label="Customer service agent wearing a headset" style="background:linear-gradient(135deg,#6fa0b0,#d6c4b2 50%,#e9eef0)"></div>
  <p>Sed pretium aliquet euismod. Quisque feugiat eleifend vulputate. Etiam turpis magna, bibendum id mollis non, condimentum ac leo. Aenean at metus at risus consectetur ullamcorper.</p>
  <div class="more">more info <svg width="17" height="17" viewBox="0 0 17 17"><circle cx="8.5" cy="8.5" r="8.5" fill="var(--icon)"/><path d="M7 5l4 3.5-4 3.5z" fill="#fff"/></svg></div>
</section>

<section class="feature" style="left:634px">
  <h3>Videos</h3>
  <div class="photo" role="img" aria-label="Worker in a warehouse aisle, video preview" style="background:linear-gradient(135deg,#5a3a24,#a9835b 50%,#3d2a1c)">
    <svg width="184" height="134" viewBox="0 0 184 134" style="position:absolute;left:0;top:0"><circle cx="92" cy="64" r="23" fill="#fff" opacity="0.9"/><circle cx="92" cy="64" r="18" fill="#333"/><path d="M86 54l16 10-16 10z" fill="#fff"/></svg>
  </div>
  <p>Donec hendrerit, risus sed bibendum iaculis, urna lectus malesuada turpis, vel gravida arcu libero vitae nulla. Integer fringilla interdum sagittis. Nunc lacus quam, consequat at mollis feugiat.</p>
  <div class="more">more info <svg width="17" height="17" viewBox="0 0 17 17"><circle cx="8.5" cy="8.5" r="8.5" fill="var(--icon)"/><path d="M7 5l4 3.5-4 3.5z" fill="#fff"/></svg></div>
</section>

<section class="about">
  <div class="about-col" style="left:33px">
    <h2>Who we are?</h2>
    <p>Etiam lacinia ultricies vehicula. Nam sagittis augue vel nisl laoreet in gravida nibh pretium. Donec a ipsum urna, sit amet suscipit massa. Maecenas ultricies condimentum est vitae tempor. Integer at sem urna. Morbi tincidunt porttitor diam. Vestibulum ante ipsum primis in faucibus orci luctus et ultrices posuere cubilia Curaeimperdiet.</p>
  </div>
  <div class="about-col" style="left:433px">
    <h2>Why us?</h2>
    <p>Suspendisse pellentesque convallis aliquam. Donec pharetra lectus a urna pharetra porta. Mauris lacus nulla, volutpat id sagittis nec, eleifend quis odio. Pellentesque fermentum vehicula aliquam. Suspendisse placerat gravida risus nec varius. In rutrum ultrices ligula. Donec interdum egestas odio, at elementum erat eleifend sed.</p>
  </div>
</section>

<footer class="site-footer">
  <div class="footer-brand">Harborline Movers</div>
  <div class="copyright">© Copyright 2012</div>
  <nav class="main-nav footer-nav">
    <a class="current" href="#" style="text-decoration:none">Home</a><a href="#">About us</a><a href="#">Services</a><a href="#">Products</a><a href="#">Partners</a><a href="#">News</a><a href="#">Contacts</a>
  </nav>
</footer>

</body>
</html>
```